Swimming Pool Supply Company Business Cards

We need business cards designed for company. These need to be easy to edit so that we can fill in names, titles, and contact info for each person who works here.

Dalton R. Whitfield
Manager of Legal & Finance
K.L. Brisbane, Incorporated

4837 Grenway Avenue
Marlow Heights, PA 19243

E. dalton@klbrisbane-example.com
M. (215) 555-0173
O. (215) 555-0148

Contact Information for Business Card

Looking to upgrade current business cards with graphic that can be edited. Looking for fresh ideas for an age old industry.

Font styles to use
Serif
Sans Serif

Colors

Designer to choose colors to be used in the design.

Requirements
Must have
• Professional, fresh, unique but professional

```html
<!DOCTYPE html>
<html lang="en">
<head>
<meta charset="utf-8">
<title>K.L. Brisbane Business Card</title>
<link rel="stylesheet" href="https://fonts.googleapis.com/css2?family=Roboto:wght@400;700&display=swap">
<style>
  :root {
    --backdrop: #3b3b3d;
    --card: #232326;
    --card-front: #1f1f22;
    --ink: #ffffff;
    --ink-soft: #e6e6e6;
    --mark-grey: #5a5a5e;
    --accent: #0a90d8;
    --edge-grey: #8a8a8c;
  }
  * { box-sizing: border-box; margin: 0; padding: 0; }
  html, body {
    width: 799px; height: 1200px; overflow: hidden;
    background: var(--backdrop);
    font-family: "Roboto", sans-serif;
  }
  .card {
    position: absolute; left: 90px;
    width: 620px; height: 354px;
    border-radius: 22px; overflow: hidden;
    box-shadow: 0 14px 30px rgba(0,0,0,.45);
  }
  .card-front { top: 110px; background: var(--card-front); }
  .card-back { top: 700px; background: var(--card); }

  .front-wordmark {
    position: absolute; inset: 0;
    display: flex; align-items: center; justify-content: center;
    font-weight: 700; font-size: 72px; letter-spacing: 2px;
    color: var(--mark-grey);
  }

  .wordmark {
    position: absolute; left: 38px; top: 26px;
    font-weight: 700; font-size: 62px; letter-spacing: 1px;
    color: var(--ink);
  }
  .tagline {
    position: absolute; left: 40px; top: 104px;
    font-size: 15px; color: var(--ink-soft);
  }
  .person { position: absolute; left: 40px; top: 146px; }
  .person-name { font-weight: 700; font-size: 22px; color: var(--accent); }
  .person-title { font-size: 15px; color: var(--ink-soft); margin-top: 3px; }
  .address {
    position: absolute; left: 40px; top: 216px;
    font-size: 15px; line-height: 21px; color: var(--ink-soft);
    font-style: normal;
  }
  .contacts {
    position: absolute; left: 312px; top: 170px;
    list-style: none; font-size: 15px; color: var(--ink);
  }
  .contacts li { display: flex; align-items: center; height: 22px; }
  .contacts svg { width: 14px; height: 14px; margin-right: 12px; fill: var(--accent); }

  .edge-strip {
    position: absolute; left: 0; bottom: 0; width: 100%; height: 12px;
    background: var(--edge-grey);
  }
  .company-band {
    position: absolute; right: 0; bottom: 0;
    width: 390px; height: 62px;
    background: var(--accent);
    border-top-left-radius: 30px;
    display: flex; align-items: center; justify-content: center;
    font-size: 17px; color: var(--ink);
  }
</style>
</head>
<body>

<section class="card card-front" aria-label="Card front">
  <div class="front-wordmark">BRISBANE</div>
</section>

<section class="card card-back" aria-label="Card back">
  <div class="wordmark">BRISBANE</div>
  <p class="tagline">Big Enough to Serve You, Small Enough to Care</p>

  <div class="person">
    <p class="person-name">Dalton R. Whitfield</p>
    <p class="person-title">Manager of Legal &amp; Finance</p>
  </div>

  <address class="address">
    4837 Grenway Avenue<br>
    Marlow Heights, PA 19243
  </address>

  <ul class="contacts">
    <li>
      <svg viewBox="0 0 14 14" aria-hidden="true"><path d="M4 0h6a1 1 0 0 1 1 1v12a1 1 0 0 1-1 1H4a1 1 0 0 1-1-1V1a1 1 0 0 1 1-1zm0 2v9h6V2z"/></svg>
      (215) 555-0173
    </li>
    <li>
      <svg viewBox="0 0 14 14" aria-hidden="true"><path d="M1 4c0-2 2-3 6-3s6 1 6 3v1H9V4H5v1H1zM3 6h8l2 6H1z"/></svg>
      (215) 555-0148
    </li>
    <li>
      <svg viewBox="0 0 14 14" aria-hidden="true"><path d="M0 3h14v8H0zm1 1v.5l6 4 6-4V4z"/></svg>
      dalton@klbrisbane-example.com
    </li>
    <li>
      <svg viewBox="0 0 14 14" aria-hidden="true"><path d="M7 0a7 7 0 1 1 0 14A7 7 0 0 1 7 0zm0 1.5a5.5 5.5 0 0 0-5.4 4.5h10.8A5.5 5.5 0 0 0 7 1.5zM1.6 8a5.5 5.5 0 0 0 10.8 0z"/></svg>
      www.klbrisbane-example.com
    </li>
  </ul>

  <div class="edge-strip"></div>
  <div class="company-band">K.L. Brisbane, Incorporated</div>
</section>

</body>
</html>
```